Refresh of a rather different IT outfit website

Our web site is starting to show it's age. You can see the existing site here: www.plumbcorner.net. As a growing company we want to come across as a dynamic collection of IT experts.

We want to update the design so are open to any colour palette and look, but want to retain our current table logo. We use the logo on our business cards but with a white background - see the attached file, so you don't need to keep the brown or the green.

The design should consider the range of browsers that will be looking at the site - so please show how it will look on a wide screen laptop and a 768x1024 tablet.

We want to add some pages about our team and their skills, probably with photos of each person on the team.

This is an uncoded project - the PSD files of the design is required, not coding.
Updates

Thanks everyone for the submissions so far.  It's a holiday day in the UK today but we will get some feedback on the designs so far out to you.

Target Market(s)

Architects and other creative types looking for IT support

Industry/Entity Type

Business

Font styles to use
Serif
Sans Serif

Requirements
Must have
• Must look good on a laptop and an iPad.

```html
<!DOCTYPE html>
<html lang="en">
<head>
<meta charset="utf-8">
<title>plumbcorner – IT Support &amp; Management</title>
<link href="https://fonts.googleapis.com/css2?family=Questrial&family=Open+Sans:wght@400;600;700&display=swap" rel="stylesheet">
<style>
:root{
  --plum:#8e1a55;
  --plum-light:#b0306f;
  --ink:#333;
  --muted:#777;
  --nav:#4a4a4a;
  --nav-dark:#333;
  --paper:#ffffff;
  --mist:#efefef;
  --rule:#d6d6d6;
  --footer:#4f4f4f;
  --footer-dark:#2e2e2e;
  --footer-text:#cfcfcf;
}
*{box-sizing:border-box;margin:0;padding:0}
html,body{width:1200px;height:2548px;overflow:hidden}
body{background:var(--paper);font-family:"Open Sans",sans-serif;color:var(--ink);position:relative}
.top-line{position:absolute;left:0;top:0;width:1200px;height:8px;background:var(--plum)}
.header{position:absolute;left:0;top:8px;width:1200px;height:216px}
.brand{position:absolute;left:64px;top:40px;display:flex;align-items:center;gap:16px}
.brand-mark{width:40px;height:40px;background:var(--plum)}
.brand-name{font-family:"Questrial",sans-serif;font-size:50px;color:var(--plum);letter-spacing:-1px}
.brand-tag{position:absolute;left:122px;top:104px;font-family:"Questrial",sans-serif;font-size:15px;color:var(--muted);letter-spacing:1px}
.social{position:absolute;right:64px;top:56px;display:flex;gap:8px}
.social span{width:24px;height:24px;border-radius:50%;background:var(--plum)}
.social span:nth-child(2){background:#6b6b6b}
.search{position:absolute;right:64px;top:112px;width:200px;height:26px;border:1px solid var(--rule);font-size:12px;color:#999;padding:5px 10px;font-family:"Questrial",sans-serif}
.nav{position:absolute;left:64px;top:168px;width:1088px;height:40px;background:linear-gradient(#5a5a5a,var(--nav-dark));border-radius:6px;display:flex;align-items:center;padding-left:12px}
.nav a{color:#fff;text-decoration:none;font-family:"Questrial",sans-serif;font-size:17px;padding:0 34px;line-height:40px;border-right:1px solid #666}
.nav a.active{background:var(--plum)}
.hero{position:absolute;left:0;top:224px;width:1200px;height:496px;background:linear-gradient(90deg,#f4f4f4,#e2e2e2 60%,#d0d0d0)}
.hero-art{position:absolute;left:60px;top:40px;width:520px;height:430px;background:radial-gradient(ellipse at center,var(--plum-light),var(--plum) 70%);border-radius:48% 52% 44% 56%/52% 46% 54% 48%}
.hero-copy{position:absolute;left:608px;top:108px}
.hero-copy h1{font-family:"Questrial",sans-serif;font-weight:400;color:var(--plum);font-size:34px;letter-spacing:1px}
.hero-copy ul{list-style:none;margin-top:24px}
.hero-copy li{font-family:"Questrial",sans-serif;font-size:18px;color:#444;line-height:36px;padding-left:26px;position:relative}
.hero-copy li::before{content:"";position:absolute;left:0;top:13px;width:10px;height:10px;background:#e0a02a}
.hero-band{position:absolute;left:0;top:720px;width:1200px;height:40px;background:linear-gradient(#555,#bbb 60%,var(--mist))}
.welcome{position:absolute;left:0;top:760px;width:1200px;height:700px;background:var(--mist)}
.section-title{position:absolute;left:0;width:1200px;text-align:center;font-family:"Questrial",sans-serif;font-size:34px;color:#555;letter-spacing:1px}
.section-title b{color:var(--plum);font-weight:400}
.cards{position:absolute;left:64px;top:120px;width:1072px;height:480px;display:grid;grid-template-columns:1fr 1fr;grid-template-rows:1fr 1fr}
.card{position:relative;padding:28px 0 0 160px;border-color:var(--rule);border-style:solid;border-width:0}
.card:nth-child(1){border-right-width:1px;border-bottom-width:1px}
.card:nth-child(2){border-bottom-width:1px;padding-left:184px}
.card:nth-child(3){border-right-width:1px}
.card:nth-child(4){padding-left:184px}
.card-icon{position:absolute;left:24px;top:28px;width:104px;height:104px;border-radius:50%;background:var(--plum);display:flex;align-items:center;justify-content:center}
.card:nth-child(even) .card-icon{left:48px}
.card h3{font-family:"Questrial",sans-serif;font-weight:400;font-size:17px;color:#444;letter-spacing:1px}
.card p{font-size:13px;color:var(--muted);line-height:20px;margin-top:8px;width:340px}
.btn{display:inline-block;margin-top:14px;background:var(--nav-dark);color:#fff;font-size:11px;padding:5px 14px;border-radius:3px;font-family:"Questrial",sans-serif}
.btn.plum{background:var(--plum);padding:8px 22px}
.about-title{top:1490px}
.about-title::before,.about-title::after{content:"";position:absolute;top:22px;width:330px;height:1px;background:var(--rule)}
.about-title::before{left:64px}.about-title::after{right:64px}
.about-copy{position:absolute;left:120px;top:1600px;width:420px}
.about-copy h2{font-size:30px;line-height:36px;color:#333;font-weight:700}
.about-copy p{font-size:14px;color:var(--muted);line-height:22px;margin-top:18px}
.monitor{position:absolute;left:600px;top:1600px;width:460px;height:440px}
.screen{position:absolute;left:0;top:0;width:460px;height:300px;background:#222;border-radius:8px;padding:14px}
.screen-photo{width:100%;height:100%;background:linear-gradient(135deg,#dfe6ee,#9eb0c4)}
.chin{position:absolute;left:0;top:300px;width:460px;height:40px;background:linear-gradient(#e6e6e6,#c8c8c8);border-radius:0 0 8px 8px}
.stand{position:absolute;left:190px;top:340px;width:80px;height:70px;background:linear-gradient(#ccc,#aaa)}
.foot{position:absolute;left:150px;top:408px;width:160px;height:10px;background:#bbb;border-radius:4px}
.partners{position:absolute;left:0;top:2060px;width:1200px;height:120px;background:var(--mist);display:flex;align-items:center;justify-content:center;gap:70px}
.partners span{width:140px;height:34px;background:#9a9a9a;border-radius:4px}
.footer{position:absolute;left:0;top:2180px;width:1200px;height:332px;background:var(--footer);color:var(--footer-text)}
.fcol{position:absolute;top:60px}
.fcol h4{font-family:"Questrial",sans-serif;font-weight:400;font-size:18px;color:#fff;letter-spacing:1px;margin-bottom:18px}
.fcol ul{list-style:none;font-size:12px;line-height:30px;columns:2;column-gap:40px}
.fcol li::before{content:"› "}
.footer-brand{position:absolute;right:64px;top:120px;display:flex;align-items:center;gap:12px;white-space:nowrap}
.footer-brand span{width:30px;height:30px;background:#bbb;flex:none}
.footer-brand b{font-family:"Questrial",sans-serif;font-weight:400;font-size:34px;color:#ddd}
.copyright{position:absolute;left:0;top:2512px;width:1200px;height:36px;background:var(--footer-dark);color:#aaa;font-size:11px;text-align:center;line-height:36px;letter-spacing:1px}
</style>
</head>
<body>
<div class="top-line"></div>
<header class="header">
  <div class="brand"><span class="brand-mark"></span><span class="brand-name">plumbcorner</span></div>
  <div class="brand-tag">a rather different IT outfit</div>
  <div class="social"><span></span><span></span><span></span></div>
  <div class="search">Keyword Search</div>
  <nav class="nav">
    <a class="active">HOME</a><a>ABOUT US</a><a>WHAT WE DO</a><a>NEWS BLOG</a><a>ARTICLES</a><a>CLIENTS</a><a>PARTNERS</a>
  </nav>
</header>

<section class="hero">
  <div class="hero-art" role="img" aria-label="Cloud shape made of magenta technology icons"></div>
  <div class="hero-copy">
    <h1>IT SUPPORT &amp; MANAGEMENT</h1>
    <ul>
      <li>Client/ Server Networks</li>
      <li>Cabling &amp; Wireless Solutions</li>
      <li>Data &amp; Voice Convergence</li>
      <li>Security &amp; Penetration testing</li>
      <li>Multi-site Connectivity</li>
    </ul>
  </div>
</section>
<div class="hero-band"></div>

<section class="welcome">
  <h2 class="section-title" style="top:56px">WELCOME TO <b>PLUMBCORNER</b></h2>
  <div class="cards">
    <div class="card">
      <div class="card-icon"><svg width="50" height="44" viewBox="0 0 50 44"><circle cx="25" cy="12" r="9" fill="#fff"/><rect x="10" y="24" width="30" height="18" rx="8" fill="#fff"/></svg></div>
      <h3>WHO WE ARE</h3>
      <p>Lorem ipsum dolor sit amet, consectetur adipiscing elit. Fusce vestibulum dui vitae tincidunt, a placerat ipsum feugiat. Aliquam vehicula tortor tellus interdum ut vitae tincidunt a placerat.</p>
      <span class="btn">Read more</span>
    </div>
    <div class="card">
      <div class="card-icon"><svg width="46" height="46" viewBox="0 0 46 46"><rect x="4" y="10" width="32" height="32" fill="#fff"/><circle cx="36" cy="26" r="7" fill="#fff"/><circle cx="20" cy="8" r="7" fill="#fff"/></svg></div>
      <h3>WHAT WE DO</h3>
      <p>Lorem ipsum dolor sit amet, consectetur adipiscing elit. Fusce vestibulum dui vitae tincidunt, a placerat ipsum feugiat. Aliquam vehicula tortor tellus interdum ut vitae tincidunt a placerat.</p>
      <span class="btn">Read more</span>
    </div>
    <div class="card">
      <div class="card-icon"><svg width="46" height="40" viewBox="0 0 46 40"><rect x="2" y="2" width="42" height="36" rx="3" fill="none" stroke="#fff" stroke-width="3"/><rect x="8" y="9" width="12" height="10" fill="#fff"/><path d="M24 11h14M24 17h14M8 25h30M8 31h30" stroke="#fff" stroke-width="3"/></svg></div>
      <h3>ARTICLES</h3>
      <p>Lorem ipsum dolor sit amet, consectetur adipiscing elit. Fusce vestibulum dui vitae tincidunt, a placerat ipsum feugiat. Aliquam vehicula tortor tellus interdum ut vitae tincidunt a placerat.</p>
      <span class="btn">Read more</span>
    </div>
    <div class="card">
      <div class="card-icon"><svg width="50" height="44" viewBox="0 0 50 44"><path d="M4 16c0-10 42-10 42 0v4h-10v-5c-6-2-16-2-22 0v5H4z" fill="#fff"/><path d="M12 20h26l6 20H6z" fill="#fff"/><circle cx="25" cy="30" r="5" fill="#8e1a55"/></svg></div>
      <h3>CONTACT US</h3>
      <p>Lorem ipsum dolor sit amet, consectetur adipiscing elit. Fusce vestibulum dui vitae tincidunt, a placerat ipsum feugiat. Aliquam vehicula tortor tellus interdum ut vitae tincidunt a placerat.</p>
      <span class="btn">Read more</span>
    </div>
  </div>
</section>

<h2 class="section-title about-title">ABOUT <b>PLUMBCORNER</b></h2>
<section class="about-copy">
  <h2>Lorem ipsum dolor sit amet consectetur adipiscing elit.</h2>
  <p>Duis molestie augue ac metus dignissim aliquet semper semper sapien. In auctor lobortis erat vel placerat. Nunc tempor eget velit vel blandit.</p>
  <p>Ut euismod placerat eros ut ullamcorper. Nam venenatis mattis ligula sit amet lacinia semper semper sapien. In auctor lobortis erat vel placerat.</p>
  <span class="btn plum" style="margin-top:28px">READ MORE</span>
</section>
<div class="monitor">
  <div class="screen"><div class="screen-photo" role="img" aria-label="Office team gathered around a laptop"></div></div>
  <div class="chin"></div><div class="stand"></div><div class="foot"></div>
</div>

<section class="partners" aria-label="Partners"><span></span><span></span><span></span><span></span><span></span></section>

<footer class="footer">
  <div class="fcol" style="left:140px">
    <h4>NAVIGATION</h4>
    <ul><li>HOME</li><li>ABOUT US</li><li>WHAT WE DO</li><li>NEWS BLOG</li><li>ARTICLES</li><li>CLIENTS</li><li>PARTNERS</li></ul>
  </div>
  <div class="fcol" style="left:448px">
    <h4>SUPPORT</h4>
    <ul style="columns:1"><li>DOCUMENTATION</li><li>CUSTOMER SERVICE</li><li>FAQ</li><li>PRODUCT INFORMATION</li></ul>
  </div>
  <div class="fcol" style="left:704px">
    <h4>FOLLOW US</h4>
    <ul style="columns:1"><li>FRIENDBOOK</li><li>CHIRPLINE</li><li>WORKLINKER</li></ul>
  </div>
  <div class="footer-brand"><span></span><b>plumbcorner</b></div>
</footer>
<div class="copyright">COPYRIGHT © 2014 PLUMB CORNER. ALL RIGHTS RESERVED</div>
</body>
</html>
```